Packaging box designs for Halvorn Crest, a series of five designs for automotive parts

We need a series of five packaging box designs for an a start up in Orange County CA named "Halvorn Crest". Winner will be contracted for future product design. We are an remanufactured autoparts wholesaler focusing on five product lines: Starters, Alternators, Engine Control Units (ECU), Transmission Control Units (TCU), and Transmission Valvebodies. We would like the designer to design a series of packaging boxes with the same theme for each of the product lines. This series of remanufactured products will be marketed under the "Halvorn Rebuilt" trademark (logo attached). We want a clean and simple design theme that reflect environmental consciousness and technology/precision. We would like the primary color of our company to be used on the design (blue and white). We would like to include the company logo, the product name, and a blueprint schematic of the product (if possible, doesn't have to be exact, general schematic outline would do). Beyond that, a minimalist approach is preferred. For each product box, there will be six faces on the exterior available for design, with the possibility of one of the interior face (though not all faces need to have features). All five product boxes should carry the same over all theme, design layout, color and font choices to ensure consistent brand identity. All designs will be printed on roll end tuck top (RETT) mailer boxes (sample box drawing included, box dimensions are not accurate in sample and differ from product to product). Sample pictures of each products are attached for reference.

Target Market(s)

Mechanics, autoparts retailer, autoparts wholesaler, autoparts rebuilders.

Industry/Entity Type

Automotive

Requirements
Must have
• Company logo, trademark name (Halvorn Rebuilt), name of product (starter, alternator, etc)
Nice to have
• We like a design style similar to that of Zentab accessories, where the box is plain white with a simple view of the product displayed. If possible, we'd like the display to be in some kind of blueprint schematic format. If designer could incorporate the company and trademark color scheme it would be a plus.

```html
<!DOCTYPE html>
<html lang="en">
<head>
<meta charset="UTF-8">
<title>Halvorn Rebuilt – Valve Body Box Panels</title>
<link href="https://fonts.googleapis.com/css2?family=Exo+2:wght@300;600&display=swap" rel="stylesheet">
<style>
  :root {
    --page: #ffffff;
    --face: #e9e9e9;
    --face-top: #eeeeee;
    --face-end: #e2e2e2;
    --edge: #d4d4d4;
    --frame: #6e6e6e;
    --brand-blue: #2f8fc6;
    --ink: #2b2b2b;
    --label: #4a4a4a;
  }
  html, body {
    margin: 0;
    width: 1200px;
    height: 880px;
    overflow: hidden;
    background: var(--page);
    font-family: "Exo 2", sans-serif;
  }
  .panel {
    position: absolute;
    box-sizing: border-box;
    border: 1px solid var(--edge);
  }
  .panel-top {
    left: 280px;
    top: 60px;
    width: 880px;
    height: 240px;
    background: var(--face-top);
    border-top: 3px solid var(--brand-blue);
  }
  .panel-end {
    left: 40px;
    top: 300px;
    width: 240px;
    height: 440px;
    background: var(--face-end);
  }
  .panel-front {
    left: 280px;
    top: 300px;
    width: 880px;
    height: 440px;
    background: var(--face);
  }

  /* brand lockup shared by all panels */
  .brand-lockup {
    display: flex;
    flex-direction: column;
    align-items: center;
    gap: 8px;
  }
  .brand-mark {
    width: 46px;
    height: 46px;
    background: var(--brand-blue);
  }
  .brand-name {
    font-weight: 600;
    font-size: 24px;
    letter-spacing: 2px;
    color: var(--ink);
    text-transform: uppercase;
    white-space: nowrap;
    line-height: 1;
  }

  .panel-top .brand-lockup {
    position: absolute;
    left: 50%;
    top: 50%;
    transform: translate(-50%, -50%) rotate(180deg);
  }
  .panel-end .brand-lockup {
    position: absolute;
    left: 50%;
    top: 50%;
    transform: translate(-50%, -50%) rotate(90deg);
  }
  .panel-end .brand-mark {
    width: 38px;
    height: 38px;
  }
  .panel-end .brand-name {
    font-size: 20px;
  }

  /* front panel */
  .face-frame {
    position: absolute;
    left: 0;
    top: 0;
  }
  .panel-front .brand-lockup {
    position: absolute;
    left: 14px;
    top: 18px;
    padding: 8px 14px;
    background: var(--face);
  }
  .product-schematic {
    position: absolute;
    right: 80px;
    top: 70px;
    width: 230px;
    height: 140px;
    background: linear-gradient(135deg, #f3f3f3, #cfcfcf);
  }
  .product-name {
    position: absolute;
    right: 70px;
    bottom: 58px;
    padding: 0 10px;
    background: var(--face);
    font-weight: 300;
    font-size: 36px;
    letter-spacing: 2px;
    color: var(--label);
    text-transform: uppercase;
    line-height: 1;
  }
</style>
</head>
<body>
  <section class="panel panel-top">
    <div class="brand-lockup">
      <div class="brand-mark"></div>
      <div class="brand-name">Halvorn Rebuilt</div>
    </div>
  </section>

  <section class="panel panel-end">
    <div class="brand-lockup">
      <div class="brand-mark"></div>
      <div class="brand-name">Halvorn Rebuilt</div>
    </div>
  </section>

  <section class="panel panel-front">
    <svg class="face-frame" width="880" height="440" viewBox="0 0 880 440">
      <rect x="40" y="40" width="800" height="360" rx="28" ry="28"
            fill="none" stroke="var(--frame)" stroke-width="2.5"/>
    </svg>

    <div class="brand-lockup">
      <div class="brand-mark"></div>
      <div class="brand-name">Halvorn Rebuilt</div>
    </div>

    <div class="product-schematic" role="img" aria-label="Line drawing schematic of a transmission valve body"></div>

    <div class="product-name">Valve Body</div>
  </section>
</body>
</html>
```